Software Specialist in Artificial Intelligence innovation needs a smart and professional looking bus

Prefers a clean and professional design, yet portraying a class of its own and a world-class feel. We develop state-of-the-art software automation engines by deploying artificial intelligence that simulates the smartest brains that are able to simulate a human consultant and/or data scientist. Both single-sided or double-sided design is acceptable. Do not refer too much to our current website as we are also in the process of revamping it so that it better reflects who we are and what we do.
Updates

Project Deadline Extended
Reason: A substantial number of designs submitted to date deviates a fair bit from requirements and expectations. Feedbacks will be provided to all parties by today and as such, an extension is catered to accomodate re-submissions.

Target Market(s)

Software technology companies, software developers, enterprise clients that requires automation supported by Artificial Intelligence driven software solutions.

Industry/Entity Type

Software

Contact Information for Business Card

Marcus Tan
Chief Innovator
marcustan@veltrixia.com
mobile: +65 94567312
Company Name: Veltrixia Pte Ltd
Address: 14 Sorbank Road #05-11 Harlowe Point, Singapore 538422
Telephone: +65 63417250
Website: www.Veltrixia.com
Please do not include the titles of the above fields.

Font styles to use
Sans Serif
Other font styles liked:
• Calibri, Futura Condensed

Requirements
Must have
• Portrays a professional and innovative image. Should reflect that the company is into Artificial Intelligence software development, high tech kind of feel.
Nice to have
• A plus point would be if you can even come up with a new company logo for us, representing who we are. Our current company logo is attached.
Should not have
• Fanciful stuffs as it must portray a professional image. Prefers not to have the cloud "image" as part of the logo or in the name card.

```html
<!DOCTYPE html>
<html lang="en">
<head>
<meta charset="utf-8">
<title>Veltrixia Business Card</title>
<link rel="stylesheet" href="https://fonts.googleapis.com/css2?family=Open+Sans:wght@400;600;700;800&display=swap">
<style>
  :root {
    --bg: #ecebe8;
    --card: #ffffff;
    --ink: #2b2b2b;
    --ink-soft: #555555;
    --accent: #d8262e;
    --band: #1f1f1f;
    --rule: #bdbdbd;
    --on-band: #ffffff;
  }
  * { margin: 0; padding: 0; box-sizing: border-box; }
  html, body {
    width: 1200px; height: 1200px; overflow: hidden;
    background: var(--bg);
    font-family: "Open Sans", Arial, sans-serif;
    color: var(--ink);
  }
  .card {
    position: absolute;
    width: 820px; height: 470px;
    background: var(--card);
    border-radius: 28px;
    overflow: hidden;
    box-shadow: 0 6px 22px rgba(0,0,0,0.12);
  }
  .card--front { left: 90px; top: 80px; }
  .card--back { left: 290px; top: 650px; }

  .brand { display: flex; align-items: center; gap: 12px; }
  .brand__dot { width: 24px; height: 24px; border-radius: 50%; background: var(--accent); }
  .brand__name { font-weight: 800; font-size: 64px; letter-spacing: -1.5px; color: var(--ink); line-height: 1; }
  .tagline { font-weight: 700; font-size: 25px; color: var(--ink); margin-top: 10px; letter-spacing: -0.2px; white-space: nowrap; }

  .card--front .identity { position: absolute; left: 68px; top: 56px; }

  .details { position: absolute; top: 215px; left: 0; width: 100%; display: flex; }
  .address {
    width: 390px; text-align: right; padding-right: 26px;
    font-size: 17px; line-height: 1.75; color: var(--ink-soft);
    font-style: normal;
    border-right: 1px solid var(--rule);
  }
  .contacts { padding-left: 20px; list-style: none; font-size: 17px; line-height: 1.75; color: var(--ink-soft); }
  .contacts li { display: flex; align-items: center; gap: 10px; }
  .contacts svg { width: 16px; height: 16px; flex: none; }

  .footer-band { position: absolute; left: 0; bottom: 0; width: 820px; height: 110px; }
  .signature {
    position: absolute; right: 40px; bottom: 26px;
    color: var(--on-band); font-size: 25px; font-weight: 700;
    white-space: nowrap;
  }
  .signature__role { font-size: 18px; font-weight: 400; }

  .card--back .identity {
    position: absolute; left: 0; top: 110px; width: 100%;
    display: flex; flex-direction: column; align-items: center;
  }
  .card--back .brand__name { font-size: 78px; }
  .card--back .tagline { font-size: 29px; }
  .website {
    position: absolute; left: 0; width: 100%; top: 360px; text-align: center;
    font-size: 21px; letter-spacing: 5px; color: var(--ink-soft);
  }
</style>
</head>
<body>

<section class="card card--front">
  <div class="identity">
    <div class="brand">
      <span class="brand__name">Veltrixia</span>
      <span class="brand__dot"></span>
    </div>
    <p class="tagline">Engineering the next Smart Enterprise</p>
  </div>

  <div class="details">
    <address class="address">
      14 Sorbank Road #05-11<br>
      Harlowe Point<br>
      Singapore 538422
    </address>
    <ul class="contacts">
      <li>
        <svg viewBox="0 0 16 16" aria-hidden="true"><circle cx="8" cy="8" r="8" fill="var(--accent)"/><path d="M5 4.5c.6-.5 1.2-.4 1.5.2l.6 1.2c.2.4 0 .8-.3 1l-.4.3c.4 1 1.1 1.7 2.1 2.2l.3-.4c.3-.3.7-.4 1-.2l1.2.6c.6.3.7.9.2 1.5-.8.9-2.1 1-3.5 0C6.3 10 5 8.6 4.4 7c-.4-1-.2-1.9.6-2.5z" fill="#fff"/></svg>
        +65 63417250
      </li>
      <li>
        <svg viewBox="0 0 16 16" aria-hidden="true"><circle cx="8" cy="8" r="8" fill="var(--accent)"/><rect x="4" y="5" width="8" height="6" rx="1" fill="#fff"/><path d="M4.3 5.4 8 8.3l3.7-2.9" stroke="var(--accent)" stroke-width="1" fill="none"/></svg>
        marcustan@veltrixia.com
      </li>
      <li>
        <svg viewBox="0 0 16 16" aria-hidden="true"><circle cx="8" cy="8" r="8" fill="var(--accent)"/><circle cx="8" cy="8" r="4" fill="none" stroke="#fff" stroke-width="1.1"/><path d="M4 8h8M8 4c-1.6 2.4-1.6 5.6 0 8M8 4c1.6 2.4 1.6 5.6 0 8" stroke="#fff" stroke-width="0.9" fill="none"/></svg>
        www.veltrixia.com
      </li>
    </ul>
  </div>

  <svg class="footer-band" viewBox="0 0 820 110" aria-hidden="true">
    <polygon points="0,44 476,44 466,60 0,60" fill="var(--accent)"/>
    <polygon points="0,64 464,64 458,74 0,74" fill="var(--band)"/>
    <polygon points="0,110 0,82 456,82 480,32 820,32 820,110" fill="var(--band)"/>
  </svg>
  <p class="signature">Marcus Tan, <span class="signature__role">Chief Innovator</span></p>
</section>

<section class="card card--back">
  <div class="identity">
    <div class="brand">
      <span class="brand__name">Veltrixia</span>
      <span class="brand__dot"></span>
    </div>
    <p class="tagline">Engineering the next Smart Enterprise</p>
  </div>
  <p class="website">www.veltrixia.com</p>
</section>

</body>
</html>
```